KVT Website Homepage Redesign

My website needs a homepage redesign and banner photos updates for Discovery and SEO Services pages. We sell Search Engine Optimization services. We use Search Engine Optimization techniques to help our clients rank high in search engines like Zorvix. It is an intense competition to consistently rank above other businesses. The problem is there is no easy way to show what the benefits of Search Engine Optimization services look like in an emotional way. I want to use an image from sailboat racing to dramatize that our clients win at Search Engine Optimization marketing.
The following products are desired:
1. Desktop version homepage redesign with a banner that clearly shows we sell Search Engine Optimization services using sailboat racing as a metaphor.
2. Mobile version homepage redesign with a banner that clearly shows we sell Search Engine Optimization services using sailboat racing as a metaphor.
2. New banner photo for the Discovery Page
3. New banner photo for the SEO page
The design must be responsive and show well on desktops, laptops, tablets and mobile phones. The current footer style must be kept. A third service called SEO must be added.
the website URL is www.brightfernlabs.example
Target Market(s)
Business to Business
Industry/Entity Type
Digital Marketing
Coding
Coded - Design and coding required
Number of Pages Required
1 page
Colors
Designer to choose colors to be used in the design.
Look and feel
Each slider illustrates characteristics of the customer's brand and the style your logo design should communicate.

```html
<!DOCTYPE html>
<html lang="en">
<head>
<meta charset="utf-8">
<title>KVT Digital – Home</title>
<link href="https://fonts.googleapis.com/css2?family=Montserrat:wght@400;500;600&display=swap" rel="stylesheet">
<style>
:root{
  --blue:#3d74be;
  --yellow:#f5cc23;
  --light:#eef5fa;
  --ink:#1f2a36;
  --body:#3b4550;
  --ring:#c9dcef;
}
*{box-sizing:border-box;margin:0;padding:0}
html,body{width:1200px;height:2984px;overflow:hidden;background:#fff}
body{font-family:"Montserrat",sans-serif;color:var(--ink)}
.page{position:relative;width:1200px;height:2984px;overflow:hidden}
.abs{position:absolute}
.backdrop{position:absolute;left:0;top:0}
.center{left:0;width:1200px;text-align:center}
.btn{position:absolute;height:32px;border-radius:16px;font-size:12px;font-weight:500;display:flex;align-items:center;justify-content:center}
.btn-blue{background:var(--blue);color:#fff}
.btn-yellow{background:var(--yellow);color:var(--ink)}
.brand{font-weight:500;color:var(--blue);line-height:1}
/* header */
.nav a{position:absolute;top:32px;font-size:12.5px;color:var(--ink);text-decoration:none}
.nav a.active{color:var(--blue)}
.nav .phone{color:var(--blue);font-size:14px;top:30px;display:flex;gap:6px;align-items:center}
/* hero */
.hero-kicker{left:88px;top:192px;color:var(--yellow);font-size:18px}
.hero-title{left:88px;top:240px;width:440px;color:#fff;font-size:23.5px;font-weight:600;line-height:29px}
/* sections */
.h2{font-size:28px;font-weight:500;color:var(--ink)}
.lead{font-size:12.5px;line-height:19px;color:var(--body)}
.svc{position:absolute;width:232px;top:1254px;height:295px;text-align:center}
.svc.active{border:1px solid var(--blue);background:#f4f9fd}
.svc .ring{position:absolute;left:66px;top:23px;width:98px;height:98px;border-radius:50%;border:7px solid var(--ring);background:#fff}
.svc.active .ring{border-color:var(--blue)}
.svc .ring svg{position:absolute;left:21px;top:21px}
.svc h3{position:absolute;top:140px;width:100%;font-size:17.5px;font-weight:500}
.svc p{position:absolute;top:170px;left:12px;width:208px;font-size:12px;line-height:17.5px;color:var(--body)}
.svc .more{position:absolute;top:258px;width:100%;font-size:12px;font-weight:600;color:var(--blue)}
.who{position:absolute;top:1896px;width:240px;text-align:center;font-size:15.5px;font-weight:500;line-height:20px}
.who svg{display:block;margin:0 auto 12px}
.quote{position:absolute;top:2214px;width:290px;font-size:12.5px;line-height:21px;color:var(--body)}
.quote h4{font-size:14px;font-weight:500;color:var(--ink);margin-top:20px}
.quote .visit{font-size:13px;color:var(--blue);margin-top:6px}
.badge{position:absolute;top:2206px;width:128px;height:128px;border-radius:50%;background:#fff;box-shadow:0 6px 20px rgba(61,116,190,.12);display:flex;align-items:center;justify-content:center;gap:6px;font-size:13px;font-weight:600;color:var(--blue)}
.badge i{width:10px;height:10px;background:var(--yellow);border-radius:50%}
/* footer */
.foot-h{font-size:17.5px;font-weight:500}
.links a{display:block;font-size:12.5px;color:var(--body);text-decoration:none;height:24px}
.field{position:absolute;width:240px;height:30px;border-radius:15px;background:#e3ecf4;font-size:11.5px;color:#7a8794;padding:9px 18px}
.social{position:absolute;top:2933px;width:32px;height:32px;border-radius:50%;background:#e3ecf4}
.social.on{background:var(--yellow)}
</style>
</head>
<body>
<div class="page">

<svg class="backdrop" width="1200" height="2984" viewBox="0 0 1200 2984" aria-hidden="true">
  <defs>
    <linearGradient id="sea" x1="0" y1="0" x2="0" y2="1">
      <stop offset="0" stop-color="#6f86a6"/>
      <stop offset=".45" stop-color="#a9b9cc"/>
      <stop offset=".7" stop-color="#3e5677"/>
      <stop offset="1" stop-color="#1f3a5e"/>
    </linearGradient>
  </defs>
  <!-- services band -->
  <path d="M0 1030 Q300 1110 570 1106 Q900 1100 1200 1020 L1200 1730 L0 1730Z" fill="var(--light)"/>
  <path d="M0 984 Q280 1080 570 1106 Q300 1100 0 1030Z" fill="var(--blue)"/>
  <!-- who section -->
  <path d="M0 1730 Q300 1690 570 1702 Q900 1740 1200 1855 L1200 2067 L0 2067Z" fill="#fff"/>
  <path d="M560 1702 Q900 1712 1200 1790 L1200 1855 Q900 1738 560 1702Z" fill="var(--blue)"/>
  <rect x="0" y="2066" width="1200" height="2" fill="#eef2f6"/>
  <!-- footer band -->
  <path d="M0 2470 Q300 2570 580 2577 Q900 2570 1200 2465 L1200 2984 L0 2984Z" fill="var(--light)"/>
  <path d="M0 2420 Q250 2540 580 2577 Q300 2562 0 2470Z" fill="var(--blue)"/>
  <rect x="88" y="2918" width="1024" height="1" fill="#d5e0ea"/>
</svg>

<!-- hero photo area -->
<svg class="abs" style="left:0;top:80px" width="1200" height="620" viewBox="0 0 1200 620" role="img" aria-label="Photo of racing sailboats heeling over on a bright blue sea">
  <rect width="1200" height="560" fill="url(#sea)"/>
  <path d="M0 480 Q120 520 260 525 Q360 528 400 560 Q500 620 620 600 Q720 580 820 545 Q960 500 1060 478 Q1140 465 1200 470 L1200 620 L0 620Z" fill="var(--yellow)"/>
  <path d="M0 520 Q140 560 260 556 Q350 556 390 590 Q470 640 620 620 L0 620Z M620 620 Q760 590 860 540 Q1000 500 1200 518 L1200 620Z" fill="#fff"/>
</svg>

<!-- header -->
<header class="abs" style="left:0;top:0;width:1200px;height:80px;background:#fff">
  <div class="abs brand" style="left:88px;top:16px;font-size:24px">KVT<br><span style="font-size:17px;font-weight:400">Digital</span></div>
  <nav class="nav">
    <a class="active" style="left:320px">Home</a>
    <a style="left:396px">About Us</a>
    <a style="left:492px">Services</a>
    <a style="left:582px">Testimonials</a>
    <a style="left:698px">Let's Talk</a>
    <span class="abs phone" style="left:806px">
      <svg width="14" height="14" viewBox="0 0 24 24" fill="none" stroke="currentColor" stroke-width="2"><path d="M5 3h4l2 5-2.5 1.5a11 11 0 0 0 6 6L16 13l5 2v4a2 2 0 0 1-2 2A16 16 0 0 1 3 5a2 2 0 0 1 2-2z"/></svg>+123 555 0147</span>
  </nav>
  <div class="btn btn-blue" style="left:984px;top:24px;width:128px">Contact Us</div>
</header>

<div class="abs hero-kicker">Are you ready to take the lead?</div>
<h1 class="abs hero-title">It’s KVT Digital’s mission to empower every client with the web presence that will drive them ahead of the competition.</h1>
<div class="btn btn-yellow" style="left:88px;top:389px;width:128px">Contact Now!</div>

<!-- mission -->
<h2 class="abs center h2" style="top:744px;line-height:35px">Our mission is to empower every client with the<br>web presence that will drive them</h2>
<p class="abs center lead" style="top:847px">We enable businesses to take the lead online with websites built on a smart foundation and with the robust features and<br>digital strategy that give every client the competitive edge needed in today’s world.</p>
<p class="abs center lead" style="top:905px">Our team of industry experts allows you to have a one-stop-shop for business discovery, website strategy,<br>advanced SEO, design and development, content creation, marketing, hosting, and technical support. Whether your project<br>requires a digital marketer, web strategist, copywriter or editor, multi-media producer ...</p>
<div class="btn btn-blue" style="left:536px;top:996px;width:128px">About Us</div>

<!-- services -->
<h2 class="abs center h2" style="top:1186px">Services We Provide</h2>
<svg class="abs" style="left:34px;top:1395px" width="22" height="18" viewBox="0 0 22 18" fill="none" stroke="var(--ink)" stroke-width="1.6"><path d="M21 9H2M9 2L2 9l7 7"/></svg>
<svg class="abs" style="left:1145px;top:1395px" width="22" height="18" viewBox="0 0 22 18" fill="none" stroke="var(--ink)" stroke-width="1.6"><path d="M1 9h19M13 2l7 7-7 7"/></svg>

<div class="svc" style="left:88px">
  <div class="ring"><svg width="42" height="42" viewBox="0 0 42 42" fill="none" stroke="var(--blue)" stroke-width="2"><rect x="12" y="4" width="18" height="12" rx="2"/><path d="M4 26h34M10 26v12M32 26v12M16 20h10v6"/></svg></div>
  <h3>SEO Consulting</h3>
  <p>A website built with a strong SEO base is essential. Powerful search engine optimization means higher ...</p>
  <div class="more">Read More &nbsp;→</div>
</div>
<div class="svc active" style="left:352px">
  <div class="ring"><svg width="42" height="42" viewBox="0 0 42 42" fill="none" stroke="var(--yellow)" stroke-width="2.2"><rect x="4" y="6" width="34" height="24" rx="2"/><path d="M10 13h10M10 19h14M10 24h8M16 36h10M21 30v6"/></svg></div>
  <h3>Website Strategy</h3>
  <p>A strong company website increases leads and reduces bounces by giving a visitor exactly exactly ...</p>
  <div class="more">Read More &nbsp;→</div>
</div>
<div class="svc" style="left:616px">
  <div class="ring"><svg width="42" height="42" viewBox="0 0 42 42" fill="none" stroke="var(--blue)" stroke-width="2"><circle cx="18" cy="18" r="11"/><circle cx="18" cy="18" r="4"/><path d="M26 26l11 11"/></svg></div>
  <h3>Local Optimization</h3>
  <p>When online audiences can find businesses in their own backyard to answer all of their needs, your business ...</p>
  <div class="more">Read More &nbsp;→</div>
</div>
<div class="svc" style="left:880px">
  <div class="ring"><svg width="42" height="42" viewBox="0 0 42 42" fill="none" stroke="var(--blue)" stroke-width="2"><rect x="4" y="6" width="34" height="30" rx="2"/><path d="M4 13h34M10 20h12M10 26h8M24 32l10-12"/></svg></div>
  <h3>Web Writing Services</h3>
  <p>Well-crafted web writing is a balancing act between message, brand voice, audience expecta-tion, and SEO ...</p>
  <div class="more">Read More &nbsp;→</div>
</div>
<div class="btn btn-yellow" style="left:536px;top:1590px;width:128px">View All</div>

<!-- who -->
<h2 class="abs center h2" style="top:1773px">Who Do We Work With?</h2>
<p class="abs center lead" style="top:1826px">There are many variations of passages of Lorem Ipsum available, but the majority have suffered alteration<br>some form, by injected humour, or randomised words which don't look</p>
<div class="who" style="left:84px"><svg width="38" height="36" viewBox="0 0 38 36" fill="none" stroke="var(--blue)" stroke-width="2"><path d="M2 34h34V4L2 14z M2 24l10-6 8 6 16-10"/></svg>Startups</div>
<div class="who" style="left:348px"><svg width="40" height="36" viewBox="0 0 40 36" fill="none" stroke="var(--blue)" stroke-width="2"><rect x="2" y="8" width="36" height="26" rx="2"/><path d="M14 8V3h12v5M2 20h36M20 18v4"/></svg>Small to Medium-Sized<br>Businesses</div>
<div class="who" style="left:612px"><svg width="40" height="36" viewBox="0 0 40 36" fill="none" stroke="var(--blue)" stroke-width="2"><path d="M20 14s-7-5-7-9a4 4 0 0 1 7-2 4 4 0 0 1 7 2c0 4-7 9-7 9zM2 26l8-6h10l6 4H14M2 34l10-4h12l14-10"/></svg>Nonprofits<br>Government Agencies</div>
<div class="who" style="left:876px"><svg width="40" height="36" viewBox="0 0 40 36" fill="none" stroke="var(--blue)" stroke-width="2"><path d="M2 4h6l5 20h20l4-14H10"/><circle cx="15" cy="31" r="3"/><circle cx="31" cy="31" r="3"/></svg>ECommerce<br>Marketplaces</div>

<!-- testimonials -->
<h2 class="abs center h2" style="top:2138px">What Our Clients Say</h2>
<svg class="abs" style="left:70px;top:2263px" width="20" height="16" viewBox="0 0 20 16" fill="none" stroke="#b8c4cf" stroke-width="1.6"><path d="M19 8H2M8 2L2 8l6 6"/></svg>
<svg class="abs" style="left:1110px;top:2263px" width="20" height="16" viewBox="0 0 20 16" fill="none" stroke="#b8c4cf" stroke-width="1.6"><path d="M1 8h17M12 2l6 6-6 6"/></svg>
<div class="badge" style="left:142px"><i></i>Lumora</div>
<div class="quote" style="left:284px">Elliot Marsh is an author, noted Leadership curriculum designer and trainer to top-tier companies. After completing his book, he decided to focus his career on curric-ulum development for customers that require train-the-trainer services and leadership coaching ...
  <h4>Institute for Growth Studies</h4><div class="visit">Visit Site &nbsp;→</div></div>
<div class="badge" style="left:642px"><i></i>Lumora</div>
<div class="quote" style="left:784px">As a surgeon in private practice, I seek to maintain a competitive edge in the areas of medical and business management technolo-gies. Therefore, I was an early adopter of electronic medical records.<br>I selected Carver and his team to analyze my workflow processes to determine ...
  <h4>Clearpath Medical Care</h4><div class="visit">Visit Site &nbsp;→</div></div>
<div class="btn btn-blue" style="left:536px;top:2462px;width:128px">View All</div>

<!-- footer -->
<footer>
  <div class="abs brand" style="left:88px;top:2638px;font-size:36px">KVT<br><span style="font-size:24px;font-weight:400">Digital</span></div>
  <div class="abs" style="left:88px;top:2718px;font-size:16px">Call Us: +123 555 0147</div>
  <div class="abs" style="left:88px;top:2747px;font-size:12.5px;color:var(--body)">e. info@kvtdigital.example</div>
  <div class="abs" style="left:88px;top:2791px;font-size:12.5px;line-height:22px;color:var(--body)">482 Harbor Crest Way<br>Suite 210B Marlow Bay,<br>MD 20614</div>

  <div class="abs foot-h" style="left:351px;top:2657px">Quick Links</div>
  <div class="abs links" style="left:352px;top:2720px"><a>Home</a><a>About Us</a><a>Services</a><a>Testimonials</a><a>Let's Talk</a><a>Contact Us</a></div>
  <div class="abs links" style="left:467px;top:2720px"><a>Terms of Use</a><a>Privacy</a></div>

  <div class="abs foot-h" style="left:616px;top:2657px">Are you Ready to Take the Lead?</div>
  <div class="field" style="left:616px;top:2725px">Name</div>
  <div class="field" style="left:872px;top:2725px">Phone</div>
  <div class="field" style="left:616px;top:2773px">Email Address</div>
  <div class="field" style="left:872px;top:2773px">Company Name</div>
  <div class="btn btn-yellow" style="left:616px;top:2820px;width:111px">Submit</div>

  <div class="abs" style="left:88px;top:2942px;font-size:12px;color:var(--body)">© 2020 <span style="color:var(--blue)">KVT Digital.</span> All Rights Reserved</div>
  <div class="abs" style="left:827px;top:2940px;font-size:14px;font-weight:500">Connect With Us</div>
  <div class="social" style="left:964px"></div>
  <div class="social on" style="left:1002px"></div>
  <div class="social" style="left:1040px"></div>
  <div class="social" style="left:1078px"></div>
</footer>

</div>
</body>
</html>
```